New Years Greeting Card Design Competition

We need a greeting card design for the new year 2014. We would like to have pictures of our daughter Meera on the card. Please find attached 5 photos of her. Please feel free to use all 5 or some of them for the design. We would like the following text on the card: "Happy New Year" and "Vikram, Sunita, and Meera Bhattachar." We would like to see designs that are very positive in style.

Target Market(s)

The greeting card is going to be sent to family and friends in different parts of the world.

Requirements
Must have
• We would like to have pictures of our daughter Meera on the card. Please find attached 5 photos of her. Please feel free to use all 5 or some of them for the design. We would like the following text on the card: "Happy New Year" and "Vikram, Sunita, and Meera Bhattachar."

```html
<!DOCTYPE html>
<html lang="en">
<head>
<meta charset="utf-8">
<title>Happy New Year – Vikram, Sunita, and Meera Bhattachar</title>
<link rel="stylesheet" href="https://fonts.googleapis.com/css2?family=Berkshire+Swash&display=swap">
<style>
  :root {
    --cream-light: #fbf5dc;
    --cream: #f3e8c2;
    --gold-soft: #eadba8;
    --gold-deep: #e2cf92;
    --greeting-pink: #f06fa8;
    --frame-pink: #f07ab0;
    --name-purple: #9a62c9;
    --glow-white: #ffffff;
    --photo-light: #eef1f4;
    --photo-lavender: #b4a4dc;
  }
  * { margin: 0; padding: 0; box-sizing: border-box; }
  html, body { width: 1200px; height: 900px; overflow: hidden; background: var(--cream); }
  .card {
    position: relative;
    width: 1200px;
    height: 900px;
    overflow: hidden;
    background: linear-gradient(135deg, var(--cream-light) 0%, var(--cream) 45%, var(--gold-soft) 100%);
  }
  .snowflake-backdrop {
    position: absolute;
    inset: 0;
    background:
      radial-gradient(circle at 15% 12%, rgba(255,255,255,0.85) 0%, rgba(255,255,255,0) 14%),
      radial-gradient(circle at 40% 6%, rgba(255,255,255,0.7) 0%, rgba(255,255,255,0) 12%),
      radial-gradient(circle at 62% 14%, rgba(255,255,255,0.6) 0%, rgba(255,255,255,0) 11%),
      radial-gradient(circle at 92% 8%, rgba(255,255,255,0.75) 0%, rgba(255,255,255,0) 13%),
      radial-gradient(circle at 6% 48%, rgba(255,255,255,0.7) 0%, rgba(255,255,255,0) 12%),
      radial-gradient(circle at 48% 48%, rgba(255,255,255,0.55) 0%, rgba(255,255,255,0) 10%),
      radial-gradient(circle at 10% 78%, rgba(255,255,255,0.8) 0%, rgba(255,255,255,0) 15%),
      radial-gradient(circle at 32% 72%, rgba(255,255,255,0.55) 0%, rgba(255,255,255,0) 12%),
      radial-gradient(circle at 58% 88%, rgba(255,255,255,0.6) 0%, rgba(255,255,255,0) 12%),
      radial-gradient(circle at 96% 60%, rgba(255,255,255,0.55) 0%, rgba(255,255,255,0) 10%),
      radial-gradient(circle at 88% 92%, rgba(255,255,255,0.7) 0%, rgba(255,255,255,0) 13%),
      radial-gradient(circle at 26% 30%, rgba(226,207,146,0.45) 0%, rgba(226,207,146,0) 14%),
      radial-gradient(circle at 22% 92%, rgba(226,207,146,0.5) 0%, rgba(226,207,146,0) 14%),
      radial-gradient(circle at 78% 4%, rgba(226,207,146,0.45) 0%, rgba(226,207,146,0) 12%),
      radial-gradient(circle at 100% 35%, rgba(226,207,146,0.5) 0%, rgba(226,207,146,0) 14%);
  }
  .sparkle {
    position: absolute;
    width: 44px;
    height: 44px;
    margin: -22px 0 0 -22px;
    border-radius: 50%;
    background: radial-gradient(circle, rgba(255,255,255,1) 0%, rgba(255,255,255,0.85) 18%, rgba(255,255,255,0) 70%);
    pointer-events: none;
  }
  .greeting {
    position: absolute;
    left: 40px;
    top: 262px;
    width: 560px;
    text-align: center;
    font-family: "Berkshire Swash", cursive;
    font-weight: 400;
    font-size: 116px;
    line-height: 126px;
    color: var(--greeting-pink);
    text-shadow: 0 0 10px var(--glow-white), 0 0 22px var(--glow-white), 0 0 34px rgba(255,255,255,0.8);
  }
  .photo-frame {
    position: absolute;
    left: 605px;
    top: 127px;
    width: 563px;
    height: 612px;
    filter: drop-shadow(0 6px 10px rgba(90, 70, 40, 0.35)) drop-shadow(0 0 14px rgba(255,255,255,0.9));
  }
  .photo-frame svg { display: block; width: 100%; height: 100%; }
  .family-names {
    position: absolute;
    left: 0;
    top: 806px;
    width: 1156px;
    text-align: center;
    font-family: "Berkshire Swash", cursive;
    font-weight: 400;
    font-size: 44px;
    line-height: 56px;
    color: var(--name-purple);
    text-shadow: 0 0 8px var(--glow-white), 0 0 16px var(--glow-white);
  }
</style>
</head>
<body>
  <main class="card">
    <div class="snowflake-backdrop" role="img" aria-label="Soft golden snowflake pattern background"></div>

    <h1 class="greeting">Happy<br>New Year!</h1>

    <div class="photo-frame">
      <svg viewBox="-10 -10 580 630" xmlns="http://www.w3.org/2000/svg">
        <defs>
          <clipPath id="bracket-clip">
            <path d="M60,24 Q280,-10 500,24 Q520,50 536,50 Q572,305 536,560 Q520,560 500,586 Q280,620 60,586 Q40,560 24,560 Q-12,305 24,50 Q40,50 60,24 Z"/>
          </clipPath>
          <linearGradient id="photo-tones" x1="0" y1="0" x2="0" y2="1">
            <stop offset="0" stop-color="var(--photo-light)"/>
            <stop offset="0.3" stop-color="#dcd6d6"/>
            <stop offset="0.48" stop-color="#d6bfae"/>
            <stop offset="0.62" stop-color="#c6b8e0"/>
            <stop offset="1" stop-color="var(--photo-lavender)"/>
          </linearGradient>
        </defs>
        <g clip-path="url(#bracket-clip)">
          <rect x="-20" y="-20" width="600" height="660" fill="url(#photo-tones)" role="img" aria-label="Photo of baby Meera wrapped in a lavender knitted blanket"/>
        </g>
        <path d="M60,24 Q280,-10 500,24 Q520,50 536,50 Q572,305 536,560 Q520,560 500,586 Q280,620 60,586 Q40,560 24,560 Q-12,305 24,50 Q40,50 60,24 Z"
              fill="none" stroke="var(--frame-pink)" stroke-width="11"/>
      </svg>
    </div>

    <span class="sparkle" style="left:250px; top:240px;"></span>
    <span class="sparkle" style="left:405px; top:398px;"></span>
    <span class="sparkle" style="left:75px; top:435px;"></span>
    <span class="sparkle" style="left:1035px; top:135px;"></span>
    <span class="sparkle" style="left:683px; top:645px;"></span>

    <p class="family-names">Vikram, Sunita, and Meera Bhattachar</p>
  </main>
</body>
</html>
```